Company brochure for our unique consulting business

We are a small consulting business offering a unique set of services to our clients.. In simple terms we are a business improvement consultancy helping our clients get the best out of their businesses. We work with clients across multiple sectors and deliver a variety of services. We want to put together a brochure to cover these main themes:1. Who we are2. What we do3. The type of people we employ4. The sectors we work inWhile the brochure needs to have a certain corporate feel to it, we don't want it to be "boring" or "stiff". We would like it to have a slightly "friendly" or "informal" feel to it, to reflect the type of organisation we are.We have a company website http://tollandvergeadvisory.com , however we do not want to directly replicate the content or feel as we recognise it needs updating.We would like the brochure to be A4 portrait format. We anticipate requiring 12 sides (including covers) but we are happy to be guided on this based on the content we have provided.The attached ppt file gives the detail of the content to be included and also shows the proposed pagination. For the front cover we would like to try 2 versions, one with the TVA logo and one with the Tolland Verge Advisory logo (a file of both is attached)One of the most important pages will be the "Our Services" page. We would like this to cover the centre fold. In the ppt file we have shown an example layout, but this is where we need most help - we are clearly not graphic designers! This page will be the most used page in sales meetings etc.Also attached is the following:1. file for our TollandVerge Advisory company logo.2. File for our TVA company logo3. Files for Derek's signatures (for under photos) - Owen's to follow4. Photo of Derek & Owen (person in purple shirt to be cropped out)Thank you and really excited to see what everyone comes back with.Derek & Owen

Target Market(s)

Very broad - Manufacturing, Healthcare, Hospitality

Industry/Entity Type

Management Consulting

Font styles to use
Other font styles liked:
• We use Swiss721, but happy to be guided by designer

Colors
3276b5
85abd2
0355a3
333333
5c5c5c
9d9d9d
d9d9d9

Requirements
Must have
• Corporate feel
Nice to have
• Slightly friendly feel
• Our standard "blue" is (CORRECTION) - R55 G96 B146 #376092 and our standard grey is R197 G178, B179 - #B3B2B2, which we would like to keep, but other colours we are happy to be guided on. Brand guidelines attached.

```html
<!DOCTYPE html>
<html lang="en">
<head>
<meta charset="utf-8">
<title>Tolland Verge Advisory – Brochure Covers</title>
<link href="https://fonts.googleapis.com/css2?family=Arimo:wght@400;700&display=swap" rel="stylesheet">
<style>
  :root{
    --brand-blue:#376092;
    --band-blue:#5479a8;
    --brand-grey:#b3b2b2;
    --ink:#1f1f1f;
    --ink-soft:#333333;
    --paper:#ffffff;
    --backdrop:#e8ebf0;
    --photo-light:#d9d9d9;
    --photo-dark:#9d9d9d;
  }
  *{margin:0;padding:0;box-sizing:border-box}
  html,body{width:899px;height:1200px;overflow:hidden}
  body{background:var(--backdrop);font-family:"Arimo",Arial,sans-serif;color:var(--ink);position:relative}

  .spread{position:absolute;left:50px;width:800px;height:566px;background:var(--paper);
    box-shadow:0 6px 18px rgba(0,0,0,.18);overflow:hidden}
  .spread--logo-short{top:24px}
  .spread--logo-long{top:610px}
  .spread::after{content:"";position:absolute;left:399px;top:0;width:2px;height:100%;
    background:linear-gradient(to right,rgba(0,0,0,.08),rgba(0,0,0,0))}

  .page{position:absolute;top:0;width:400px;height:566px}
  .page--back{left:0}
  .page--front{left:400px}

  /* back cover */
  .back-band{position:absolute;left:0;top:150px;width:400px;height:290px;background:var(--band-blue)}
  .bar{position:absolute;width:30px;background:var(--brand-grey)}
  .bar--1{left:100px;top:210px;height:230px}
  .bar--2{left:150px;top:120px;height:210px}
  .bar--3{left:205px;top:235px;height:230px}
  .bar--4{left:258px;top:110px;height:225px}

  .contact{position:absolute;top:500px;border-left:2px solid var(--brand-blue);padding-left:7px;
    font-style:normal;font-size:8.5px;font-weight:700;line-height:1.45;color:var(--ink-soft)}
  .contact--address{left:30px}
  .contact--lines{left:205px}

  /* front cover */
  .wordmark{position:absolute;left:28px;top:34px;display:flex;align-items:center;gap:8px;
    font-weight:700;color:var(--ink);line-height:1}
  .wordmark__square{width:14px;height:14px;background:var(--brand-blue)}
  .wordmark--short .wordmark__name{font-size:38px;letter-spacing:1px}
  .wordmark--long .wordmark__name{font-size:21px;line-height:1.05}

  .stripes{position:absolute;left:240px;top:28px}
  .photo{position:absolute}
  .photo--team{left:0;top:118px;width:240px;height:215px;
    background:linear-gradient(135deg,var(--photo-light),#f2f2f2 45%,var(--photo-dark))}
  .frame-stem{position:absolute;left:240px;top:60px;width:10px;height:283px;background:var(--brand-blue)}
  .frame-base{position:absolute;left:0;top:333px;width:250px;height:10px;background:var(--brand-blue)}
  .photo--touch{left:262px;top:122px;width:130px;height:140px;border:6px solid var(--brand-blue);
    background:linear-gradient(160deg,#e6e6e6,#9d9d9d 60%,#333333)}

  .intro{position:absolute;left:24px;top:372px;width:352px}
  .intro__title{font-size:16px;font-weight:700;letter-spacing:.3px;color:var(--ink);margin-bottom:5px}
  .intro__text{font-size:8.5px;line-height:1.35;text-align:justify;color:var(--ink-soft)}
</style>
</head>
<body>

<section class="spread spread--logo-short" aria-label="Cover spread, short wordmark version">
  <div class="page page--back">
    <div class="back-band" role="img" aria-label="Blue-tinted photo of an office desk"></div>
    <div class="bar bar--1"></div><div class="bar bar--2"></div>
    <div class="bar bar--3"></div><div class="bar bar--4"></div>
    <address class="contact contact--address">TVA Limited<br>Harbour Chambers<br>Kiln Street, Derby DE1 4ZX</address>
    <address class="contact contact--lines">Tel: +44 (0) 1632 960514<br>enquiries@tollandvergegroup.com<br>www.tollandvergegroup.com</address>
  </div>
  <div class="page page--front">
    <div class="wordmark wordmark--short"><span class="wordmark__square"></span><span class="wordmark__name">TVA</span></div>
    <svg class="stripes" width="160" height="90" viewBox="0 0 160 90" aria-hidden="true">
      <rect x="14" y="0" width="14" height="90" fill="#b3b2b2"/>
      <rect x="34" y="0" width="14" height="90" fill="#376092"/>
      <rect x="54" y="0" width="14" height="90" fill="#b3b2b2"/>
      <rect x="74" y="0" width="14" height="90" fill="#376092"/>
      <rect x="94" y="0" width="14" height="90" fill="#b3b2b2"/>
      <rect x="114" y="0" width="46" height="90" fill="#b3b2b2"/>
    </svg>
    <div class="frame-stem"></div>
    <div class="photo photo--team" role="img" aria-label="Black and white photo of two consultants smiling at a meeting table"></div>
    <div class="frame-base"></div>
    <div class="photo photo--touch" role="img" aria-label="Black and white photo of a hand touching a digital diagram"></div>
    <div class="intro">
      <h2 class="intro__title">MANAGEMENT CONSULTING</h2>
      <p class="intro__text">We are a multi-disciplinary Group providing Business Support Services through four focused divisions. Our core offering of Business Improvement, Events Management, Estate Management and Recruitment are integrated with a focus on optimising the People, Process &amp; Assets of the clients we work with</p>
    </div>
  </div>
</section>

<section class="spread spread--logo-long" aria-label="Cover spread, full name version">
  <div class="page page--back">
    <div class="back-band" role="img" aria-label="Blue-tinted photo of an office desk"></div>
    <div class="bar bar--1"></div><div class="bar bar--2"></div>
    <div class="bar bar--3"></div><div class="bar bar--4"></div>
    <address class="contact contact--address">TVA Limited<br>Harbour Chambers<br>Kiln Street, Derby DE1 4ZX</address>
    <address class="contact contact--lines">Tel: +44 (0) 1632 960514<br>enquiries@tollandvergegroup.com<br>www.tollandvergegroup.com</address>
  </div>
  <div class="page page--front">
    <div class="wordmark wordmark--long"><span class="wordmark__name">Tolland Verge<br>Advisory</span><span class="wordmark__square"></span></div>
    <svg class="stripes" width="160" height="90" viewBox="0 0 160 90" aria-hidden="true">
      <rect x="14" y="0" width="14" height="90" fill="#b3b2b2"/>
      <rect x="34" y="0" width="14" height="90" fill="#376092"/>
      <rect x="54" y="0" width="14" height="90" fill="#b3b2b2"/>
      <rect x="74" y="0" width="14" height="90" fill="#376092"/>
      <rect x="94" y="0" width="14" height="90" fill="#b3b2b2"/>
      <rect x="114" y="0" width="46" height="90" fill="#b3b2b2"/>
    </svg>
    <div class="frame-stem"></div>
    <div class="photo photo--team" role="img" aria-label="Black and white photo of two consultants smiling at a meeting table"></div>
    <div class="frame-base"></div>
    <div class="photo photo--touch" role="img" aria-label="Black and white photo of a hand touching a digital diagram"></div>
    <div class="intro">
      <h2 class="intro__title">MANAGEMENT CONSULTING</h2>
      <p class="intro__text">We are a multi-disciplinary Group providing Business Support Services through four focused divisions. Our core offering of Business Improvement, Events Management, Estate Management and Recruitment are integrated with a focus on optimising the People, Process &amp; Assets of the clients we work with</p>
    </div>
  </div>
</section>

</body>
</html>
```